Management consultant needs business cards

We need a design for a personal/professional business card for a management consultant. Work is typically focused on the b2b space, helping companies improve their operations. The final design should communicate efficiency and helping companies and people achieve their full potential.

Company name is "Ashcombe Consultants"

Brand promise is "Seeing Capacity - Building Results"

We come from major consulting firms (Haldrick, Tove, JNP) but would like to project a slightly more modern feel than those players.

Target Market(s)

Targeting B2B markets such as banks or companies.

Industry/Entity Type

Business

Requirements
Must have
• The card must communicate the following information:

Neil T Marbury
Managing Director
Ashcombe Consultants
Phone: 416-782-4051
neil.marbury@ashcombeconsultants.example
www.ashcombeconsultants.example

42 Pellmore Ave
Toronto, ON M6R 2J8

Back side should have
"Seeing Capacity - Building Results"

```html
<!DOCTYPE html>
<html lang="en">
<head>
<meta charset="utf-8">
<title>Ashcombe Consultants – Business Card</title>
<link rel="stylesheet" href="https://fonts.googleapis.com/css2?family=Arimo:wght@400;700&display=swap">
<style>
  :root {
    --brand-red: #d71f27;
    --ink: #1d1d1d;
    --rule: #2a2a2a;
    --paper: #ffffff;
    --backdrop: #ecebe8;
    --card-w: 900px;
    --card-h: 500px;
  }
  * { box-sizing: border-box; margin: 0; padding: 0; }
  html, body {
    width: 1175px;
    height: 1200px;
    overflow: hidden;
    background: var(--backdrop);
    font-family: "Arimo", Arial, sans-serif;
    color: var(--ink);
  }
  .sheet {
    width: 1175px;
    height: 1200px;
    display: flex;
    flex-direction: column;
    align-items: center;
    justify-content: center;
    gap: 60px;
  }
  .card {
    position: relative;
    width: var(--card-w);
    height: var(--card-h);
    background: var(--paper);
    box-shadow: 0 6px 18px rgba(0, 0, 0, 0.18);
    overflow: hidden;
  }

  /* Back side */
  .card-back .promise-band {
    position: absolute;
    left: 0;
    right: 0;
    top: 215px;
    height: 130px;
    background: var(--brand-red);
    display: flex;
    align-items: center;
    justify-content: center;
  }
  .card-back .promise {
    color: var(--paper);
    font-size: 30px;
    font-weight: 400;
    letter-spacing: 2px;
    text-transform: uppercase;
  }

  /* Front side */
  .card-front .company {
    position: absolute;
    right: 56px;
    top: 38px;
    color: var(--brand-red);
    font-size: 27px;
    font-weight: 400;
    letter-spacing: 0.5px;
    text-transform: uppercase;
  }
  .card-front .rule {
    position: absolute;
    left: 0;
    right: 0;
    height: 4px;
    background: var(--rule);
  }
  .card-front .rule-top { top: 102px; }
  .card-front .rule-bottom { top: 206px; }
  .card-front .name {
    position: absolute;
    left: 64px;
    top: 118px;
    color: var(--brand-red);
    font-size: 36px;
    font-weight: 400;
    letter-spacing: 1px;
    text-transform: uppercase;
  }
  .card-front .title {
    position: absolute;
    left: 68px;
    top: 166px;
    font-size: 22px;
    font-weight: 400;
    text-transform: uppercase;
  }
  .card-front .phone {
    position: absolute;
    top: 232px;
    left: 0;
    right: 0;
    display: flex;
    justify-content: center;
    align-items: center;
    gap: 18px;
    font-size: 28px;
    letter-spacing: 0.5px;
  }
  .card-front .contact-col {
    position: absolute;
    top: 280px;
    text-align: center;
    font-size: 24px;
    line-height: 44px;
  }
  .card-front .contact-col svg { display: block; margin: 0 auto 4px; }
  .card-front .email-col {
    left: 10px;
    width: 440px;
    font-size: 22px;
    text-transform: uppercase;
  }
  .card-front .address-col {
    left: 480px;
    width: 400px;
    letter-spacing: 0.5px;
  }
  .card-front .web-band {
    position: absolute;
    left: 0;
    right: 0;
    bottom: 0;
    height: 50px;
    background: var(--brand-red);
    color: var(--paper);
    display: flex;
    align-items: center;
    justify-content: center;
    font-size: 23px;
    letter-spacing: 0.5px;
  }
</style>
</head>
<body>
<main class="sheet">

  <section class="card card-back" aria-label="Card back">
    <div class="promise-band">
      <p class="promise">“Seeing Capacity - Building Results”</p>
    </div>
  </section>

  <section class="card card-front" aria-label="Card front">
    <p class="company">Ashcombe Consultants</p>
    <div class="rule rule-top"></div>
    <h1 class="name">Neil T Marbury</h1>
    <p class="title">Managing Director</p>
    <div class="rule rule-bottom"></div>

    <p class="phone">
      <svg width="24" height="30" viewBox="0 0 24 30" aria-hidden="true">
        <rect x="1" y="1" width="22" height="28" rx="3" fill="var(--brand-red)"/>
        <rect x="5" y="5" width="14" height="6" fill="#fff"/>
        <g fill="#fff">
          <rect x="5" y="14" width="3.5" height="3"/><rect x="10.25" y="14" width="3.5" height="3"/><rect x="15.5" y="14" width="3.5" height="3"/>
          <rect x="5" y="19" width="3.5" height="3"/><rect x="10.25" y="19" width="3.5" height="3"/><rect x="15.5" y="19" width="3.5" height="3"/>
          <rect x="5" y="24" width="3.5" height="2.5"/><rect x="10.25" y="24" width="3.5" height="2.5"/><rect x="15.5" y="24" width="3.5" height="2.5"/>
        </g>
      </svg>
      <span>416-782-4051</span>
    </p>

    <div class="contact-col email-col">
      <svg width="30" height="22" viewBox="0 0 30 22" aria-hidden="true">
        <rect x="1" y="1" width="28" height="20" fill="var(--brand-red)"/>
        <path d="M1 1 L15 12 L29 1 M1 21 L11 9 M29 21 L19 9" stroke="#fff" stroke-width="2" fill="none"/>
      </svg>
      <p>neil.marbury@<br>ashcombeconsultants.example</p>
    </div>

    <div class="contact-col address-col">
      <svg width="30" height="22" viewBox="0 0 30 26" aria-hidden="true">
        <path d="M15 1 L29 13 L25 13 L25 25 L18 25 L18 17 L12 17 L12 25 L5 25 L5 13 L1 13 Z" fill="var(--brand-red)"/>
      </svg>
      <p>42 Pellmore Ave, Toronto,<br>ON M6R 2J8</p>
    </div>

    <div class="web-band">www.ashcombeconsultants.example</div>
  </section>

</main>
</body>
</html>
```